Cedar Hall letterhead

We changed our name and logo now need letterhead.
3-4/72 Harlow Street Elmsford 2793
www.cedarhall.org.au
info@cedarhall.org.au
ph: 02 97584120

At this stage, we are preferencing Design #: 5398880 and Design #5401338

```html
<!DOCTYPE html>
<html lang="en">
<head>
<meta charset="utf-8">
<title>Cedar Hall Letterhead</title>
<link rel="stylesheet" href="https://fonts.googleapis.com/css2?family=Jost:wght@300;400&display=swap">
<style>
  :root {
    --paper: #ffffff;
    --brand-blue: #5d8ca3;
    --footer-blue: #5b86a6;
    --rule-blue: #6f93b3;
    --tagline-grey: #e5e5e5;
  }
  * { margin: 0; padding: 0; box-sizing: border-box; }
  html, body {
    width: 848px;
    height: 1200px;
    overflow: hidden;
    background: var(--paper);
  }
  .letterhead {
    position: relative;
    width: 848px;
    height: 1200px;
    background: var(--paper);
    font-family: "Jost", "Futura", sans-serif;
  }
  .brand {
    position: absolute;
    top: 66px;
    left: 0;
    width: 100%;
    text-align: center;
    font-weight: 300;
    font-size: 34px;
    line-height: 42px;
    letter-spacing: 1px;
    color: var(--brand-blue);
    text-transform: uppercase;
  }
  .tagline {
    position: absolute;
    left: 29px;
    top: 474px;
    font-weight: 300;
    font-size: 82px;
    line-height: 104px;
    color: var(--tagline-grey);
    letter-spacing: 0.5px;
    white-space: nowrap;
  }
  .footer-rule {
    position: absolute;
    left: 25px;
    top: 1141px;
    width: 801px;
    height: 1px;
    background: var(--rule-blue);
  }
  .contact {
    position: absolute;
    left: 52px;
    top: 1147px;
    width: 744px;
    display: flex;
    justify-content: space-between;
    align-items: center;
    font-weight: 400;
    font-size: 12px;
    line-height: 16px;
    color: var(--footer-blue);
    list-style: none;
    white-space: nowrap;
  }
  .contact-sep {
    font-size: 11px;
  }
</style>
</head>
<body>
  <main class="letterhead">
    <header class="brand">Cedar Hall</header>

    <p class="tagline">SERVING ALL.<br>SHARING LIGHT.</p>

    <div class="footer-rule"></div>
    <ul class="contact">
      <li>W: www.cedarhall.org.au</li>
      <li class="contact-sep">•</li>
      <li>E: info@cedarhall.org.au</li>
      <li class="contact-sep">•</li>
      <li>A: 3-4/72 Harlow Street Elmsford 2793</li>
      <li class="contact-sep">•</li>
      <li>P: 02-97584120</li>
    </ul>
  </main>
</body>
</html>
```